TK Fiscal Website Redesign Contest

We want to refresh our website to be more insitutional, professional for an international audience. We have designed a new logo for this purpose and that has been attached. A full brand brief and positioning statement has also been attached. Please read through all the documents carefully before designing. The old website is found here: https://tk-fiscal-example.com/

Target Market(s)

Actuaries and associated businesses internationally

Industry/Entity Type

professional services - actuaries

Number of Pages Required

3 page

Font styles to use
Sans Serif

Colors
0054AA
0677BA
7BADD7
CADEEF
E8F1F8
0094D4
00A9DD
6FCCEA
C7EBF8
E9F6FB
F0912C
F2A743
F7CA91
FBE8D2
FDF5EE
EE7325
F08F49
F5BC92
FAE3D3
FDF4ED
EB3D1F
EC4F4E
F09395
F8D3D4
FCEDEE

Requirements
Must have
• blues and greens to match the logo color, complimentary colors, navigation
Nice to have
• old site: https://tk-fiscal-example.com/

```html
<!DOCTYPE html>
<html lang="en">
<head>
<meta charset="utf-8">
<title>TK Fiscal — Actuarial Software</title>
<link rel="stylesheet" href="https://fonts.googleapis.com/css2?family=Archivo:wght@600;700;800&family=Inter:wght@400;500;600&display=swap">
<style>
:root{
  --navy:#0054AA;
  --blue:#0677BA;
  --sky:#0094D4;
  --cyan:#00A9DD;
  --aqua:#6FCCEA;
  --soft:#7BADD7;
  --pale:#E8F1F8;
  --mist:#E9F6FB;
  --accent-warm:#F0912C;
  --ink:#111111;
  --text:#3a3a3a;
  --white:#ffffff;
  --footer:#0B2A4A;
}
*{box-sizing:border-box;margin:0;padding:0}
html,body{width:1200px;height:4098px;overflow:hidden}
body{position:relative;font-family:"Inter",Arial,sans-serif;color:var(--text);background:var(--white)}
.abs{position:absolute}
h1,h2,h3,.brand{font-family:"Archivo","Inter",Arial,sans-serif}
.brand{font-weight:700;letter-spacing:2px;color:var(--navy);display:flex;align-items:center;gap:10px}
.brand-dot{width:12px;height:12px;border-radius:50%;background:var(--cyan)}
.btn{position:absolute;display:flex;align-items:center;justify-content:space-between;background:var(--blue);color:#fff;border-radius:30px;font-size:14px;font-weight:500;padding:0 6px 0 24px;white-space:nowrap}
.btn .arr{width:32px;height:32px;border-radius:50%;border:2px solid #fff;display:flex;align-items:center;justify-content:center;flex:none}
.nav{top:0;left:0;width:1200px;height:70px;background:#fff;border-bottom:1px solid var(--pale)}
.nav-links{position:absolute;top:27px;font-size:13px;color:#333}
.nav-links span{position:absolute;white-space:nowrap}
.hero{top:70px;left:0;width:1200px;height:544px;background:linear-gradient(90deg,#0a1e36 0%,#0f2d52 38%,#1f5a8c 62%,#5c93c0 82%,#a9c8e2 100%)}
.hero h1{position:absolute;left:70px;top:116px;color:#fff;font-size:36px;line-height:45px;font-weight:800;width:470px}
.hero p{position:absolute;left:70px;top:312px;color:#fff;font-size:13.5px;line-height:23px;width:440px}
.section-title{position:absolute;left:0;width:1200px;text-align:center;font-size:35px;font-weight:700;color:var(--ink)}
.section-title em{font-style:normal;color:var(--sky)}
.rule{position:absolute;left:578px;width:44px;height:2px;background:var(--cyan)}
.lead{position:absolute;left:0;width:1200px;text-align:center;font-size:13.5px;line-height:23px;color:#333}
.feature{position:absolute;top:826px;width:215px;height:256px;background:#fff;border-radius:6px;box-shadow:0 2px 14px rgba(0,84,170,.10);padding:24px 22px}
.feature svg{display:block}
.feature h3{margin-top:16px;font-family:"Inter",sans-serif;font-size:14.5px;font-weight:600;color:#222;line-height:20px;height:44px}
.feature .mini{width:30px;height:2px;background:var(--cyan);margin:4px 0 22px}
.feature p{font-size:12.5px;line-height:19px;color:#555}
.band{left:0;width:1200px;background:var(--pale)}
.sol{position:absolute;left:629px;width:440px}
.sol .ic{position:absolute;left:0;top:0;width:70px;height:70px;border-radius:50%;display:flex;align-items:center;justify-content:center}
.sol h3{position:absolute;left:92px;top:3px;font-family:"Inter",sans-serif;font-size:15px;font-weight:600;color:#222}
.sol p{position:absolute;left:92px;top:28px;width:340px;font-size:12.5px;line-height:19px;color:#555}
.learn{position:absolute;font-size:12.5px;color:var(--blue);display:flex;align-items:center;gap:12px}
.char{position:absolute;width:280px}
.char h3{font-family:"Inter",sans-serif;font-size:15px;font-weight:600;color:#222;margin-bottom:6px}
.char p{font-size:12.5px;line-height:19px;color:#555}
.char.left{text-align:right}
.cbub{position:absolute;width:78px;height:78px;border-radius:50%;display:flex;align-items:center;justify-content:center}
.post{position:absolute;top:2728px;width:286px;height:367px;background:#fff;border-radius:6px;box-shadow:0 2px 12px rgba(0,84,170,.08);overflow:hidden}
.post .ph{height:191px}
.post h3{font-family:"Inter",sans-serif;font-size:15px;font-weight:600;line-height:21px;color:#111;margin:20px 18px 8px}
.post p{font-size:12.5px;line-height:19px;color:#555;margin:0 18px}
.post .learn{left:18px;bottom:33px}
.footer{top:3616px;left:0;width:1200px;height:482px;background:var(--footer)}
.cta{top:3345px;left:142px;width:917px;height:376px;border-radius:22px;background:radial-gradient(circle at 30% 25%,#1f6fb4 0%,#0d3a6b 42%,#071a30 100%)}
.cta h2{position:absolute;left:0;top:72px;width:917px;text-align:center;color:#fff;font-size:35px;line-height:44px;font-weight:800}
.cta p{position:absolute;left:0;top:175px;width:917px;text-align:center;color:#fff;font-size:13.5px;line-height:23px}
.foot-h{position:absolute;color:#fff;font-family:"Archivo",sans-serif;font-weight:700;font-size:16px;letter-spacing:.5px}
.foot-link{position:absolute;left:576px;color:#d6e4f2;font-size:12.5px}
.foot-txt{color:#d6e4f2;font-size:12.5px;line-height:19px}
.soc{position:absolute;top:4056px;width:30px;height:30px;border-radius:50%;border:2px solid #fff}
</style>
</head>
<body>

<header class="abs nav">
  <div class="brand abs" style="left:70px;top:20px;font-size:26px"><span class="brand-dot"></span>TK FISCAL</div>
  <nav class="nav-links">
    <span style="left:391px;color:var(--sky)">Home</span>
    <span style="left:461px">Platform</span>
    <span style="left:544px">Solutions</span>
    <span style="left:631px">Insights</span>
    <span style="left:712px">Company</span>
    <span style="left:802px">Contact</span>
  </nav>
  <div class="btn" style="left:882px;top:16px;width:248px;height:38px;justify-content:center;padding:0;font-size:13px">Request a Technical Walkthrough</div>
</header>

<section class="abs hero">
  <div class="abs" role="img" aria-label="Photo of three professionals reviewing charts and documents at a café table" style="left:480px;top:0;width:720px;height:544px"></div>
  <h1>ACTUARIAL SOFTWARE FOR STRUCTURED, AUDITABLE FINANCIAL ANALYSIS.</h1>
  <p><strong>TK Fiscal</strong> develops software that translates established actuarial methodologies into disciplined, decision-ready tools.</p>
  <div class="btn" style="left:70px;top:374px;width:304px;height:44px;background:var(--sky)">Request A Technical Walkthrough<span class="arr"><svg width="14" height="14" viewBox="0 0 14 14"><path d="M2 7h10M8 3l4 4-4 4" stroke="#fff" stroke-width="1.8" fill="none"/></svg></span></div>
</section>

<h2 class="section-title" style="top:683px">PLATFORM <em>OVERVIEW</em></h2>
<div class="rule" style="top:735px"></div>
<p class="lead" style="top:754px">Our platform empowers actuaries and risk professionals with tools designed for modern<br>regulatory and business demands.</p>

<div class="feature" style="left:142px">
  <svg width="48" height="48" viewBox="0 0 48 48"><rect x="6" y="6" width="36" height="26" rx="2" fill="none" stroke="var(--navy)" stroke-width="2"/><path d="M18 38h12M24 32v6" stroke="var(--navy)" stroke-width="2"/><circle cx="24" cy="17" r="5" fill="none" stroke="var(--cyan)" stroke-width="2"/></svg>
  <h3>Structured Workflows</h3><div class="mini"></div>
  <p>that guide users through every step of the analysis process</p>
</div>
<div class="feature" style="left:376px">
  <svg width="48" height="48" viewBox="0 0 48 48"><circle cx="26" cy="20" r="14" fill="none" stroke="var(--sky)" stroke-width="2"/><path d="M16 30l20-20M20 33l16-16M14 26l18-18" stroke="var(--sky)" stroke-width="1.5"/><circle cx="12" cy="38" r="4" fill="none" stroke="var(--navy)" stroke-width="2"/></svg>
  <h3>Full Transparency Of Assumptions</h3><div class="mini"></div>
  <p>that guide users through every step of the analysis process</p>
</div>
<div class="feature" style="left:610px">
  <svg width="48" height="48" viewBox="0 0 48 48"><rect x="8" y="6" width="24" height="32" rx="2" fill="none" stroke="var(--navy)" stroke-width="2"/><circle cx="30" cy="30" r="8" fill="none" stroke="var(--cyan)" stroke-width="2"/><path d="M36 36l7 7" stroke="var(--navy)" stroke-width="2.5"/><path d="M13 14h14M13 20h10" stroke="var(--navy)" stroke-width="2"/></svg>
  <h3>Built-in Auditability</h3><div class="mini"></div>
  <p>that guide users through every step of the analysis process</p>
</div>
<div class="feature" style="left:844px">
  <svg width="48" height="48" viewBox="0 0 48 48"><circle cx="24" cy="24" r="18" fill="none" stroke="var(--sky)" stroke-width="2"/><path d="M14 20l10-6 10 6M16 22v10M21 22v10M27 22v10M32 22v10M13 34h22" stroke="var(--sky)" stroke-width="2" fill="none"/></svg>
  <h3>Robust Governance Features</h3><div class="mini"></div>
  <p>that guide users through every step of the analysis process</p>
</div>

<section class="abs band" style="top:1167px;height:682px"></section>
<h2 class="section-title" style="top:1235px">CORE <em>SOLUTIONS</em></h2>
<div class="rule" style="top:1287px"></div>
<p class="lead" style="top:1307px">Precision-built modules for the most demanding actuarial tasks</p>
<div class="abs" role="img" aria-label="Photo of two hands joining wooden puzzle pieces" style="left:142px;top:1364px;width:423px;height:400px;border-radius:8px;background:linear-gradient(135deg,#eef3f8 0%,#c9d6e3 45%,#4f6478 75%,#1e2b3a 100%)"></div>

<div class="sol" style="top:1365px">
  <div class="ic" style="background:var(--navy)"><svg width="34" height="34" viewBox="0 0 34 34"><circle cx="19" cy="12" r="8" fill="none" stroke="#fff" stroke-width="2"/><path d="M19 6v6h6" stroke="#fff" stroke-width="2" fill="none"/><path d="M3 26c4-2 8-3 12-1l8 1c2 0 2 3 0 3H13" stroke="#fff" stroke-width="2" fill="none"/></svg></div>
  <h3>Reserving &amp; Valuation</h3>
  <p>Perform compliant, repeatable reserving and valuation processes with full traceability and support for multiple actuarial methods and regulatory frameworks.</p>
  <div class="learn" style="left:92px;top:96px">Learn More<svg width="16" height="10" viewBox="0 0 16 10"><path d="M0 5h14M10 1l4 4-4 4" stroke="var(--blue)" stroke-width="1.5" fill="none"/></svg></div>
</div>
<div class="sol" style="top:1513px">
  <div class="ic" style="background:var(--cyan)"><svg width="34" height="34" viewBox="0 0 34 34"><path d="M8 4h13l5 5v21H8z" fill="none" stroke="#fff" stroke-width="2"/><circle cx="22" cy="24" r="7" fill="var(--cyan)" stroke="#fff" stroke-width="2"/><path d="M12 12h8M12 17h6" stroke="#fff" stroke-width="2"/></svg></div>
  <h3>Pricing</h3>
  <p>Build and test pricing models with transparent assumptions, scenario testing, and comparative analytics to support profitable product development.</p>
  <div class="learn" style="left:92px;top:96px">Learn More<svg width="16" height="10" viewBox="0 0 16 10"><path d="M0 5h14M10 1l4 4-4 4" stroke="var(--blue)" stroke-width="1.5" fill="none"/></svg></div>
</div>
<div class="sol" style="top:1660px">
  <div class="ic" style="background:var(--navy)"><svg width="34" height="34" viewBox="0 0 34 34"><circle cx="17" cy="13" r="8" fill="none" stroke="#fff" stroke-width="2"/><path d="M17 9v5M17 16v1" stroke="#fff" stroke-width="2"/><path d="M4 28c4-2 8-3 12-1l8 1c2 0 2 3 0 3H14" stroke="#fff" stroke-width="2" fill="none"/></svg></div>
  <h3>Enterprise Risk Management</h3>
  <p>Integrate risk metrics, stress testing, and capital modeling in a governed environment to support ORSA, Solvency II, and other ERM requirements.</p>
  <div class="learn" style="left:92px;top:96px">Learn More<svg width="16" height="10" viewBox="0 0 16 10"><path d="M0 5h14M10 1l4 4-4 4" stroke="var(--blue)" stroke-width="1.5" fill="none"/></svg></div>
</div>

<h2 class="section-title" style="top:1913px">PLATFORM <em>CHARACTERISTICS</em></h2>
<div class="rule" style="top:1968px"></div>
<p class="lead" style="top:1991px">Engineered for clarity, built to scale across borders</p>

<svg class="abs" style="left:420px;top:2050px" width="356" height="356" viewBox="0 0 356 356"><circle cx="178" cy="178" r="172" fill="none" stroke="var(--aqua)" stroke-width="2"/></svg>
<div class="brand abs" style="left:468px;top:2212px;width:260px;justify-content:center;font-size:28px">TK FISCAL</div>

<div class="cbub" style="left:443px;top:2074px;background:var(--navy)"><svg width="40" height="40" viewBox="0 0 40 40"><rect x="15" y="5" width="10" height="8" fill="none" stroke="#fff" stroke-width="2"/><path d="M20 13v6M8 19h24M8 19v6M20 19v6M32 19v6" stroke="#fff" stroke-width="2" fill="none"/><rect x="4" y="25" width="8" height="7" fill="none" stroke="#fff" stroke-width="2"/><rect x="16" y="25" width="8" height="7" fill="none" stroke="#fff" stroke-width="2"/><rect x="28" y="25" width="8" height="7" fill="none" stroke="#fff" stroke-width="2"/></svg></div>
<div class="cbub" style="left:677px;top:2074px;background:var(--cyan)"><svg width="40" height="40" viewBox="0 0 40 40"><circle cx="14" cy="11" r="5" fill="none" stroke="#fff" stroke-width="2"/><path d="M24 8h10M24 13h8" stroke="#fff" stroke-width="2"/><path d="M4 32c4-3 9-4 14-2l8 1c2 0 2 3 0 3H15" stroke="#fff" stroke-width="2" fill="none"/></svg></div>
<div class="cbub" style="left:443px;top:2307px;background:var(--cyan)"><svg width="40" height="40" viewBox="0 0 40 40"><path d="M8 5h16l6 6v24H8z" fill="none" stroke="#fff" stroke-width="2"/><circle cx="19" cy="21" r="6" fill="none" stroke="#fff" stroke-width="2"/><path d="M23 25l6 6" stroke="#fff" stroke-width="2"/></svg></div>
<div class="cbub" style="left:677px;top:2307px;background:var(--navy)"><svg width="40" height="40" viewBox="0 0 40 40"><circle cx="20" cy="18" r="12" fill="none" stroke="#fff" stroke-width="2"/><path d="M15 22v-5M20 22v-9M25 22v-6" stroke="#fff" stroke-width="2"/><path d="M6 36l8-6" stroke="#fff" stroke-width="2"/></svg></div>

<div class="char left" style="left:138px;top:2082px"><h3>Structured Workflows</h3><p>Consistent, repeatable processes from<br>data to disclosure.</p></div>
<div class="char" style="left:781px;top:2082px"><h3>Multi-jurisdictional Review Support</h3><p>Localise assumptions, outputs, and reports<br>for any regulator.</p></div>
<div class="char left" style="left:138px;top:2316px"><h3>Transparent Assumptions</h3><p>Every assumption exposed, documented,<br>and linked to source.</p></div>
<div class="char" style="left:781px;top:2316px"><h3>Comparative Analysis Capability</h3><p>Run scenarios side by side — instantly see<br>impacts.</p></div>

<div class="btn" style="left:449px;top:2448px;width:302px;height:44px">Request A Technical Walkthrough<span class="arr"><svg width="14" height="14" viewBox="0 0 14 14"><path d="M2 7h10M8 3l4 4-4 4" stroke="#fff" stroke-width="1.8" fill="none"/></svg></span></div>

<section class="abs band" style="top:2575px;height:684px"></section>
<h2 class="section-title" style="top:2646px">LATEST <em>INSIGHTS</em></h2>

<article class="post" style="left:142px">
  <div class="ph" role="img" aria-label="Photo of a person working with charts, a calculator and a laptop" style="background:linear-gradient(135deg,#7fa3c2,#c9d8e4 55%,#e9eef2)"></div>
  <h3>Advancing Actuarial Methods in a Changing Regulatory Landscape</h3>
  <p>Exploring how modern tools support evolving best practices in reserving and capital modeling.</p>
  <div class="learn">Learn More<svg width="16" height="10" viewBox="0 0 16 10"><path d="M0 5h14M10 1l4 4-4 4" stroke="var(--blue)" stroke-width="1.5" fill="none"/></svg></div>
</article>
<article class="post" style="left:457px">
  <div class="ph" role="img" aria-label="Photo of hands reviewing printed charts beside a laptop" style="background:linear-gradient(135deg,#5aa9d6,#b9dcef 50%,#eef6fb)"></div>
  <h3>Governance and Documentation in Actuarial Modeling</h3>
  <p>Why audit trails and assumption transparency are critical for internal and external review.</p>
  <div class="learn">Learn More<svg width="16" height="10" viewBox="0 0 16 10"><path d="M0 5h14M10 1l4 4-4 4" stroke="var(--blue)" stroke-width="1.5" fill="none"/></svg></div>
</article>
<article class="post" style="left:772px">
  <div class="ph" role="img" aria-label="Photo of analysts reviewing data on laptops in an office" style="background:linear-gradient(135deg,#10263d,#2e4d6a 50%,#7e98ae)"></div>
  <h3>Multi-Jurisdictional Actuarial Practice: Challenges &amp; Solutions</h3>
  <p>Strategies for managing compliance across Solvency II, NAIC, and emerging frameworks.</p>
  <div class="learn">Learn More<svg width="16" height="10" viewBox="0 0 16 10"><path d="M0 5h14M10 1l4 4-4 4" stroke="var(--blue)" stroke-width="1.5" fill="none"/></svg></div>
</article>

<div class="btn" style="left:516px;top:3130px;width:168px;height:44px">Read Insights<span class="arr"><svg width="14" height="14" viewBox="0 0 14 14"><path d="M2 7h10M8 3l4 4-4 4" stroke="#fff" stroke-width="1.8" fill="none"/></svg></span></div>

<footer class="abs footer"></footer>
<section class="abs cta" role="img" aria-label="Dark photo of a hand holding a phone with a glowing globe network">
  <h2>READY TO SEE THE<br>PLATFORM IN ACTION?</h2>
  <p>Schedule a technical walkthrough and discover how TK Fiscal can bring<br>structure, transparency, and auditability to your actuarial processes.</p>
  <div class="btn" style="left:307px;top:247px;width:302px;height:44px;background:var(--sky)">Request A Technical Walkthrough<span class="arr"><svg width="14" height="14" viewBox="0 0 14 14"><path d="M2 7h10M8 3l4 4-4 4" stroke="#fff" stroke-width="1.8" fill="none"/></svg></span></div>
</section>

<div class="brand abs" style="left:142px;top:3808px;font-size:36px;color:#fff"><span class="brand-dot" style="width:16px;height:16px"></span>TK FISCAL</div>
<p class="abs foot-txt" style="left:142px;top:3882px;width:300px">Software that translates actuarial methodologies into disciplined decision-ready analytical tools across diverse regulatory environments.</p>

<div class="foot-h" style="left:576px;top:3814px">QUICK LINKS</div>
<span class="foot-link" style="top:3859px">Home</span>
<span class="foot-link" style="top:3886px">Platform</span>
<span class="foot-link" style="top:3913px">Solutions</span>
<span class="foot-link" style="top:3940px">Insights</span>
<span class="foot-link" style="top:3967px">Company</span>
<span class="foot-link" style="top:3994px">Contact</span>

<div class="foot-h" style="left:813px;top:3814px">CONTACT DETAILS</div>
<svg class="abs" style="left:813px;top:3860px" width="14" height="18" viewBox="0 0 14 18"><path d="M7 0a7 7 0 0 1 7 7c0 5-7 11-7 11S0 12 0 7a7 7 0 0 1 7-7z" fill="var(--aqua)"/><circle cx="7" cy="7" r="2.5" fill="var(--footer)"/></svg>
<div class="abs foot-txt" style="left:841px;top:3858px;width:240px"><strong style="color:#fff;font-weight:600;font-size:13.5px">TK FISCAL, Inc.</strong><br>410 Harbor Crest Ave, Suite 200<br>Bayview, FL 33100</div>
<svg class="abs" style="left:813px;top:3941px" width="16" height="16" viewBox="0 0 16 16"><path d="M3 1l3 1 1 3-2 2a9 9 0 0 0 4 4l2-2 3 1 1 3-2 2C7 15 1 9 1 3z" fill="var(--aqua)"/></svg>
<div class="abs" style="left:841px;top:3940px;color:#fff;font-size:14px">+1(555)010-2840</div>
<svg class="abs" style="left:813px;top:3982px" width="16" height="12" viewBox="0 0 16 12"><rect width="16" height="12" rx="1" fill="var(--aqua)"/><path d="M1 1l7 6 7-6" stroke="var(--footer)" stroke-width="1.4" fill="none"/></svg>
<div class="abs foot-txt" style="left:841px;top:3978px">hello@tk-fiscal-example.com</div>

<div class="abs" style="left:142px;top:4047px;width:917px;height:1px;background:#2c4e72"></div>
<div class="abs" style="left:142px;top:4063px;color:#d6e4f2;font-size:12px">© 2026 TK Fiscal. All rights reserved. &nbsp;&nbsp;&nbsp;&nbsp; Privacy · Terms</div>
<div class="soc" style="left:949px"></div>
<div class="soc" style="left:988px"></div>
<div class="soc" style="left:1027px"></div>

</body>
</html>
```